4th Generation Family Business Needs a New Card Design!

We are a family owned 4th Generation company. We are based in the Sydney, Australia area and we are desperately in need of a more modern and classy card. We are monumental masons who design, supply & erect lasting memorials throughout cemeteries in Sydney. Our customers are normally in a period of grieving. I have attached logo files that will need to be implemented on the card. Company was established 1935. Australian Owned and Operated. Card needs to be designed to PRINTLY.com specification.

Target Market(s)

Our target market is based upon people that a grieving for family members that have passed away. We also deal with alot of companies that own and operate cemeteries.

Industry/Entity Type

Business

Contact Information for Business Card

Gavin Pelham, Operations Manager, 0491726053, gavin@pelhamstoneworks.com.au
Brian Pelham, Director, 0417639285, brian@pelhamstoneworks.com.au
Phone # 02 9563 4820
Website: www.pelhamstoneworks.com.au
Address: Suite 17, 9 Lambert Lane, Kellyville, Sydney NSW 2155

Font styles to use
Serif
Decorative
Script

Requirements
Must have
• Would like to see the logo nicely implemented with a modern design. Embossed lettering would be a nice additive.

```html
<!DOCTYPE html>
<html lang="en">
<head>
<meta charset="utf-8">
<title>Pelham Stoneworks – Business Card</title>
<link href="https://fonts.googleapis.com/css2?family=Cinzel:wght@400;600&family=Tinos:wght@400&display=swap" rel="stylesheet">
<style>
  :root {
    --stage: #262626;
    --card-black: #000000;
    --card-white: #ffffff;
    --gold: #ecc22b;
    --ink: #000000;
    --paper-text: #ffffff;
  }
  html, body {
    margin: 0;
    padding: 0;
    width: 1200px;
    height: 1076px;
    overflow: hidden;
    background: var(--stage);
  }
  .canvas {
    position: relative;
    width: 1200px;
    height: 1076px;
  }
  .card {
    position: absolute;
    left: 180px;
    width: 840px;
    height: 480px;
    border-radius: 26px;
    overflow: hidden;
  }
  .card--back {
    top: 40px;
    background: var(--card-black);
  }
  .card--front {
    top: 556px;
    background: var(--card-black);
  }
  .brand {
    font-family: "Cinzel", serif;
    font-weight: 400;
    text-align: center;
    letter-spacing: 2px;
    line-height: 1.05;
  }
  .brand-mark {
    display: block;
    margin: 0 auto 26px;
    width: 46px;
    height: 46px;
  }
  .card--back .brand {
    position: absolute;
    left: 0;
    right: 0;
    top: 150px;
    color: var(--paper-text);
    font-size: 58px;
  }
  .card--back .brand-mark { background: var(--paper-text); }
  .front-art {
    position: absolute;
    inset: 0;
  }
  .brand--front {
    position: absolute;
    left: 470px;
    width: 340px;
    top: 160px;
    color: var(--ink);
    font-size: 44px;
  }
  .brand--front .brand-mark { background: var(--ink); width: 40px; height: 40px; margin-bottom: 22px; }
  .details {
    position: absolute;
    left: 32px;
    top: 74px;
    font-family: "Tinos", serif;
    color: var(--paper-text);
  }
  .person-name {
    font-family: "Cinzel", serif;
    font-weight: 600;
    font-size: 29px;
    margin: 0;
    line-height: 1;
    letter-spacing: 0.5px;
  }
  .person-role {
    color: var(--gold);
    font-size: 23px;
    margin: 0;
    line-height: 1.1;
  }
  .address {
    font-size: 23px;
    font-style: normal;
    line-height: 31px;
    margin-top: 58px;
  }
  .contacts {
    list-style: none;
    padding: 0;
    margin: 26px 0 0;
    font-size: 23px;
  }
  .contacts li {
    display: flex;
    align-items: center;
    height: 29px;
  }
  .icon {
    width: 26px;
    height: 26px;
    margin-right: 8px;
    flex: none;
  }
  .website {
    color: var(--gold);
    font-size: 22px;
    margin-top: 16px;
  }
</style>
</head>
<body>
<main class="canvas">

  <section class="card card--back" aria-label="Card back">
    <div class="brand">
      <span class="brand-mark"></span>
      Pelham<br>Stoneworks
    </div>
  </section>

  <section class="card card--front" aria-label="Card front">
    <svg class="front-art" width="840" height="480" viewBox="0 0 840 480" aria-hidden="true">
      <path d="M452 0 C 395 110, 395 370, 452 480 L 840 480 L 840 0 Z" fill="var(--gold)"/>
      <path d="M460 0 C 403 110, 403 370, 460 480 L 840 480 L 840 0 Z" fill="var(--card-white)"/>
    </svg>

    <div class="details">
      <h1 class="person-name">Gavin Pelham</h1>
      <p class="person-role">Operations Manager</p>

      <address class="address">
        Suite 17, 9 Lambert Lane,<br>
        Kellyville, Sydney NSW 2155
      </address>

      <ul class="contacts">
        <li>
          <svg class="icon" viewBox="0 0 26 26" aria-hidden="true">
            <rect width="26" height="26" rx="4" fill="var(--gold)"/>
            <rect x="8" y="4" width="10" height="18" rx="1.5" fill="#000"/>
            <rect x="10" y="6" width="6" height="5" fill="var(--gold)"/>
            <rect x="10" y="13" width="6" height="7" fill="var(--gold)" opacity="0.6"/>
          </svg>
          0491726053
        </li>
        <li>
          <svg class="icon" viewBox="0 0 26 26" aria-hidden="true">
            <rect width="26" height="26" rx="4" fill="var(--gold)"/>
            <path d="M8 5 L11 5 L12 10 L10 11.5 C11 14.5 12 16 14.5 17 L16 15 L21 16 L21 19.5 C21 20.5 20 21 19 21 C12 20 6 14 5 7 C5 6 6.5 5 8 5 Z" fill="#000"/>
          </svg>
          02 9563 4820
        </li>
        <li>
          <svg class="icon" viewBox="0 0 26 26" aria-hidden="true">
            <rect width="26" height="26" rx="4" fill="var(--gold)"/>
            <rect x="4" y="7" width="18" height="12" fill="none" stroke="#000" stroke-width="2"/>
            <path d="M4 7 L13 14 L22 7 M4 19 L10.5 12.5 M22 19 L15.5 12.5" fill="none" stroke="#000" stroke-width="1.6"/>
          </svg>
          gavin@pelhamstoneworks.com.au
        </li>
      </ul>

      <div class="website">www.pelhamstoneworks.com.au</div>
    </div>

    <div class="brand brand--front">
      <span class="brand-mark"></span>
      Pelham<br>Stoneworks
    </div>
  </section>

</main>
</body>
</html>
```